Breakthrough Medical Research company needs Podcast Album Cover

We are launching a podcast called “The Copper Lantern Podcast” with a mission to accelerate breakthroughs in Neuron Regeneration by bringing together the world’s experts in neurodegenerative diseases, spinal cord injury, and artificial intelligence. Design doesn’t need to be monochromatic but we would like it to utilize the color Blue. The design should also incorporate the Title of the podcast large enough to easily read on a small thumbnail on a phone. We’d also like the design to convey the healing or regeneration of a Neuron.

```html
<!DOCTYPE html>
<html lang="en">
<head>
<meta charset="UTF-8">
<title>The Copper Lantern Podcast — Cover</title>
<link rel="stylesheet" href="https://fonts.googleapis.com/css2?family=Barlow+Semi+Condensed:wght@600;700&display=swap">
<style>
  :root {
    --bg: #0f1112;
    --blue: #2a7fc7;
    --blue-deep: #1d5f9c;
    --white: #f3f3f3;
  }
  html, body {
    margin: 0;
    padding: 0;
    width: 1200px;
    height: 1200px;
    overflow: hidden;
    background: var(--bg);
  }
  .cover {
    position: relative;
    width: 1200px;
    height: 1200px;
    background: var(--bg);
    font-family: "Barlow Semi Condensed", sans-serif;
    overflow: hidden;
  }
  .neuron-art {
    position: absolute;
    overflow: visible;
  }
  .neuron-art--top {
    left: 40px;
    top: -40px;
    width: 680px;
    height: 380px;
  }
  .neuron-art--bottom {
    left: 930px;
    top: 780px;
    width: 340px;
    height: 460px;
  }
  .regrowth-link {
    position: absolute;
    left: 0;
    top: 0;
    width: 1200px;
    height: 1200px;
    pointer-events: none;
  }
  .regrowth-link path {
    fill: none;
    stroke: var(--blue);
    stroke-width: 5;
    stroke-linecap: round;
  }
  .regrowth-link .regrowth-link__gap {
    stroke-dasharray: 4 18;
    opacity: 0.8;
  }
  .title {
    position: absolute;
    left: 108px;
    top: 400px;
    margin: 0;
    line-height: 1;
    text-transform: uppercase;
    font-weight: 700;
  }
  .title span { display: block; }
  .title__the {
    color: var(--blue);
    font-size: 60px;
    font-weight: 600;
    margin-left: 78px;
    letter-spacing: 2px;
  }
  .title__main {
    color: var(--white);
    font-size: 220px;
    letter-spacing: 2px;
    margin-top: 6px;
    line-height: 0.9;
  }
  .title__main .title__accent {
    display: inline;
    color: var(--blue);
  }
  .title__second {
    color: var(--white);
    font-size: 150px;
    letter-spacing: 3px;
    line-height: 0.95;
    margin-top: 8px;
  }
  .title__podcast {
    color: var(--blue);
    font-size: 66px;
    font-weight: 600;
    letter-spacing: 3px;
    margin-left: 4px;
    margin-top: 14px;
  }
</style>
</head>
<body>
  <main class="cover">
    <svg class="neuron-art neuron-art--top" viewBox="0 0 680 380" role="img" aria-label="Illustration of a branching blue neuron cell regrowing its dendrites">
      <defs>
        <radialGradient id="neuronGlowTop" cx="50%" cy="50%" r="50%">
          <stop offset="0%" stop-color="#2a7fc7" stop-opacity="0.9"/>
          <stop offset="60%" stop-color="#1d5f9c" stop-opacity="0.45"/>
          <stop offset="100%" stop-color="#1d5f9c" stop-opacity="0"/>
        </radialGradient>
      </defs>
      <ellipse cx="340" cy="190" rx="320" ry="175" fill="url(#neuronGlowTop)"/>
    </svg>

    <svg class="neuron-art neuron-art--bottom" viewBox="0 0 340 460" role="img" aria-label="Illustration of a second blue neuron reaching in from the corner to reconnect">
      <defs>
        <radialGradient id="neuronGlowBottom" cx="50%" cy="50%" r="50%">
          <stop offset="0%" stop-color="#2a7fc7" stop-opacity="0.9"/>
          <stop offset="60%" stop-color="#1d5f9c" stop-opacity="0.45"/>
          <stop offset="100%" stop-color="#1d5f9c" stop-opacity="0"/>
        </radialGradient>
      </defs>
      <ellipse cx="170" cy="230" rx="160" ry="220" fill="url(#neuronGlowBottom)"/>
    </svg>

    <svg class="regrowth-link" viewBox="0 0 1200 1200" aria-hidden="true">
      <path d="M660 250 C 860 300, 1000 360, 1030 470"/>
      <path class="regrowth-link__gap" d="M1030 470 C 1060 580, 1070 680, 1080 800"/>
    </svg>

    <h1 class="title">
      <span class="title__the">The</span>
      <span class="title__main">C<span class="title__accent">o</span>pper</span>
      <span class="title__second">Lantern</span>
      <span class="title__podcast">Podcast</span>
    </h1>
  </main>
</body>
</html>
```